Speisekarten-Design für Cafe & Restaurant
Zielgruppe
Cafe & Restaurant, Geöffnet 9-18 uhr, Zielgruppe 60 % über 60 Jahre, 30% 25-50 Jahre und 10% 15-25 Jahre, Einrichtung modern in grün gelblichen pastel tönen, Speisekarten Mappen vorhanden A4 in grau.
Aufgabenstellung
Einhaltung der Speisekarten Schrift : Mark pro , Farbe der Schrift (wahrscheinlich nur bei drucken wichtig) CMYK, Vorhandene Kartenmappe (siehe foto) , wäre vom Vorteil, allerdings sind wir auch für komplett neues design offen. Das 'Vorwort' kann bzw. würde mich freuen , wenn es geändert oder schöner geschrieben wird, leider fehlen uns dafür die Ideen. Bei Fragen einfach mal kurz anschreiben. Danke

```html
<!DOCTYPE html>
<html lang="de">
<head>
<meta charset="utf-8">
<title>Speisekarte – Frühstück, Heiße Getränke, Tee</title>
<link href="https://fonts.googleapis.com/css2?family=Mulish:wght@400;600;700&display=swap" rel="stylesheet">
<style>
  :root{
    --ink:#1d1d1b;
    --green:#a9b77a;
    --grey:#8c8c8c;
    --copper:#c8925f;
    --paper:#ffffff;
  }
  *{margin:0;padding:0;box-sizing:border-box}
  html,body{width:848px;height:1200px;overflow:hidden;background:var(--paper)}
  body{font-family:"Mulish",Arial,sans-serif;color:var(--ink);position:relative}
  .page{position:relative;width:848px;height:1200px}
  .box{position:absolute}
  .box-breakfast{left:59px;top:75px;width:731px;height:188px;border:2px solid var(--green);border-radius:18px}
  .box-hot{left:64px;top:333px;width:719px;height:334px;border:2px dashed var(--grey)}
  .box-tea{left:62px;top:747px;width:725px;height:343px;border:1px solid var(--copper);border-radius:22px}
  .section-title{position:absolute;left:50%;transform:translate(-50%,-50%);top:-1px;background:var(--paper);padding:0 9px;font-weight:600;font-size:26px;line-height:1;white-space:nowrap;letter-spacing:.5px}
  .box-breakfast .section-title{color:var(--green)}
  .box-hot .section-title{color:var(--grey)}
  .box-tea .section-title{color:var(--copper)}
  .line{position:absolute;font-size:19.5px;line-height:1;white-space:nowrap;letter-spacing:.5px}
  sup{font-size:10px;vertical-align:top;position:relative;top:-3px;margin-left:3px}
  .heading{font-weight:700}
  .row{display:flex;justify-content:space-between}
  .row-left{width:272px}
  .row-right{width:370px}
  .bullet{position:absolute;font-size:14px;line-height:1}
  .decor{position:absolute;background:var(--paper)}
  .decor-cup{left:600px;top:582px;width:100px;height:100px;border-radius:50%;background:radial-gradient(circle,#bdbdbd 0%,#e4e4e4 60%,#ffffff 72%)}
  .decor-mortar{left:673px;top:1031px;width:103px;height:82px;border-radius:40% 40% 50% 50%;background:linear-gradient(160deg,#b4d146 0%,#c8925f 45%,#d9b08a 100%)}
</style>
</head>
<body>
<div class="page">

  <section class="box box-breakfast">
    <h2 class="section-title">Frühstück</h2>
    <p class="line" style="left:18px;top:37px">2 Semmeln, Butter, Marmelade, Schinken, Käse, Salami, Honig,</p>
    <p class="line" style="left:18px;top:72px">0,1 l&nbsp; Orangensaft&nbsp; + ein heißes Getränk ihrer Wahl<sup>1,2,3,4,5</sup></p>
    <p class="line" style="left:18px;top:106px">(bis 11 Uhr)</p>
    <p class="line" style="left:18px;top:141px">6,70 €</p>
  </section>

  <section class="box box-hot">
    <h2 class="section-title">Heiße Getränke</h2>

    <p class="line heading" style="left:18px;top:37px">Kaffeespezialitäten</p>
    <p class="line row row-left" style="left:18px;top:71px"><span>Tasse Kaffee<sup>7</sup></span><span>1,70 €</span></p>
    <p class="line row row-left" style="left:18px;top:106px"><span>Haferl Kaffee<sup>7</sup></span><span>2,10 €</span></p>
    <p class="line row row-left" style="left:18px;top:140px"><span>Portion Kaffee<sup>7</sup></span><span>2,80 €</span></p>
    <p class="line row row-left" style="left:18px;top:175px"><span>Espresso<sup>7</sup></span><span>1,90 €</span></p>
    <p class="line row row-left" style="left:18px;top:210px"><span>Cappuccino<sup>7</sup></span><span>2,20 €</span></p>
    <p class="line row row-left" style="left:18px;top:244px"><span>Latte Macchiato<sup>7</sup></span><span>2,60 €</span></p>
    <p class="line row row-left" style="left:18px;top:279px"><span>Haferl Milchkaffee<sup>7</sup></span><span>2,60 €</span></p>

    <p class="line heading" style="left:328px;top:37px">Schokoladen</p>
    <p class="line row row-right" style="left:328px;top:71px"><span>Schokoladen</span><span>2,60 €</span></p>
    <p class="line row row-right" style="left:328px;top:106px"><span>Heiße Schokolade mit Sahne</span><span>2,80 €</span></p>
    <p class="line row row-right" style="left:328px;top:140px"><span>Heiße Weiße Schokolade<sup>7</sup></span><span>2,80 €</span></p>
    <p class="line" style="left:328px;top:175px">Heiße Weiße Schokolade</p>
    <p class="line row row-right" style="left:328px;top:210px"><span>mit Espresso<sup>7</sup></span><span>3,50 €</span></p>
  </section>
  <div class="decor decor-cup" role="img" aria-label="Dampfende Kaffeetasse mit Untertasse"></div>

  <section class="box box-tea">
    <h2 class="section-title">Teespezialitäten</h2>
    <p class="line" style="left:25px;top:44px">Glas Tee</p>
    <p class="line" style="left:197px;top:44px">2,20 €</p>
    <p class="line" style="left:25px;top:78px">Loser Tee aus ökologischem Fairhandel Anbau serviert</p>
    <p class="line" style="left:25px;top:113px">im Glaskännchen&nbsp; 3,50 €</p>

    <span class="bullet" style="left:28px;top:151px">•</span>
    <p class="line" style="left:44px;top:148px">Darjeeling Royal</p>
    <span class="bullet" style="left:28px;top:185px">•</span>
    <p class="line" style="left:44px;top:182px">Feiner und milder</p>
    <p class="line" style="left:46px;top:205px">schwarzer Tee</p>
    <span class="bullet" style="left:28px;top:243px">•</span>
    <p class="line" style="left:44px;top:240px">Grüntee China Blatt</p>
    <span class="bullet" style="left:28px;top:277px">•</span>
    <p class="line" style="left:44px;top:274px">Weicher, zartsüsser</p>
    <p class="line" style="left:46px;top:298px">unfermentierter Tee</p>

    <span class="bullet" style="left:302px;top:151px">•</span>
    <p class="line" style="left:318px;top:148px">Rooibos Vanilla</p>
    <span class="bullet" style="left:302px;top:185px">•</span>
    <p class="line" style="left:318px;top:182px">Südafrikanischer Rotbusch, mildes Aroma</p>
    <span class="bullet" style="left:302px;top:220px">•</span>
    <p class="line" style="left:318px;top:217px">Früchtegarten</p>
    <span class="bullet" style="left:302px;top:255px">•</span>
    <p class="line" style="left:318px;top:252px">Komposition aus Hibiskus,</p>
    <p class="line" style="left:320px;top:275px">Sonnenblumenblüten, Apfel,</p>
    <p class="line" style="left:320px;top:298px">Hagebutten und Zitrus</p>
  </section>
  <div class="decor decor-mortar" role="img" aria-label="Teeschale mit Löffel und grünen Teeblättern"></div>

</div>
</body>
</html>
```